ROLL-UP DESIGN FOR SUPERMARKET DELIVERY

We need the graphic design of a roll-up with measurements 200 cm height x cm 85 width, for a supermarket delivery service.

The main logo "The Velarno" either color version or black version must be present very visible on the design.

the second logo attached 'CALVESINOSHOP' must also be present but smaller on the design.

the following text must be present on the design: CONSEGNA STESSO GIORNO.

Printing instruction attached must be respected.

Target Market(s)

HIGH END ITALIAN AND EUROPEAN SUPERMARKET CLIENTELE

Industry/Entity Type

FOOD DELIVERY

Requirements
Must have
• LOGOS ATTACHED
Nice to have
• PHOTOS OF SEA, SARDINIA, LUXURY DELIVERY, YACHTS

```html
<!DOCTYPE html>
<html lang="it">
<head>
<meta charset="utf-8">
<title>The Velarno – Roll-up Consegna Stesso Giorno</title>
<link rel="stylesheet" href="https://fonts.googleapis.com/css2?family=Poppins:wght@700;800&family=Lato:wght@700;900&display=swap">
<style>
  :root {
    --page-bg: #e4e4e4;
    --paper: #f7f7f7;
    --ink: #161616;
    --orange-deep: #ee7a1c;
    --orange-light: #fbc540;
    --orange-shadow: #b9531a;
    --accent-bar: #fcc64a;
    --sky-line: #8fd0f2;
    --charcoal: #2a2a2a;
    --charcoal-light: #4d4d4d;
    --white: #ffffff;
  }
  * { margin: 0; padding: 0; box-sizing: border-box; }
  html, body { width: 1200px; height: 994px; overflow: hidden; }
  body { background: var(--page-bg); position: relative; }

  .rollup {
    position: absolute;
    left: 400px;
    top: 27px;
    width: 400px;
    height: 940px;
    background: var(--paper);
    overflow: hidden;
    box-shadow: 0 6px 24px rgba(0,0,0,.18);
  }
  .rollup__shapes, .rollup__photo {
    position: absolute;
    inset: 0;
    width: 400px;
    height: 940px;
  }

  .brand {
    position: absolute;
    left: 0;
    top: 58px;
    width: 360px;
  }
  .brand__main {
    position: absolute;
    left: 58px;
    top: 0;
    display: flex;
    align-items: center;
    gap: 14px;
  }
  .brand__dot {
    width: 26px;
    height: 26px;
    border-radius: 50%;
    background: var(--ink);
  }
  .brand__name {
    font-family: "Poppins", sans-serif;
    font-weight: 800;
    font-size: 38px;
    letter-spacing: -1px;
    color: var(--ink);
    line-height: 1;
  }
  .brand__partner {
    position: absolute;
    right: 0;
    top: 70px;
    font-family: "Poppins", sans-serif;
    font-weight: 800;
    font-size: 25px;
    letter-spacing: -0.5px;
    color: var(--orange-deep);
    line-height: 1;
  }

  .headline {
    position: absolute;
    left: 44px;
    top: 250px;
    padding-left: 20px;
    border-left: 4px solid var(--accent-bar);
  }
  .headline__line {
    display: block;
    font-family: "Poppins", sans-serif;
    font-weight: 800;
    font-size: 49px;
    line-height: 56px;
    letter-spacing: -1.5px;
    color: var(--white);
    text-shadow: 3px 3px 0 var(--orange-shadow);
  }

  .phone {
    position: absolute;
    left: 54px;
    top: 845px;
    width: 292px;
    height: 40px;
    border-radius: 20px;
    background: var(--orange-deep);
    display: flex;
    align-items: center;
  }
  .phone__icon {
    width: 44px;
    height: 44px;
    margin-left: -4px;
    border-radius: 50%;
    background: var(--white);
    border: 3px solid var(--orange-deep);
    display: flex;
    align-items: center;
    justify-content: center;
  }
  .phone__number {
    margin-left: 12px;
    font-family: "Lato", sans-serif;
    font-weight: 900;
    font-size: 33px;
    color: var(--white);
    line-height: 1;
  }
</style>
</head>
<body>
  <main class="rollup">
    <svg class="rollup__shapes" viewBox="0 0 400 940" aria-hidden="true">
      <defs>
        <linearGradient id="orangeBand" x1="0" y1="1" x2="1" y2="0">
          <stop offset="0" stop-color="var(--orange-deep)"/>
          <stop offset="1" stop-color="var(--orange-light)"/>
        </linearGradient>
        <linearGradient id="charcoalBand" x1="0" y1="0" x2="1" y2="0">
          <stop offset="0" stop-color="var(--charcoal)"/>
          <stop offset="1" stop-color="var(--charcoal-light)"/>
        </linearGradient>
      </defs>
      <polygon class="band-dark" points="0,480 400,412 400,940 0,940" fill="url(#charcoalBand)"/>
      <polygon class="band-sky-line" points="0,488 400,418 400,424 0,494" fill="var(--sky-line)"/>
      <polygon class="band-orange" points="0,165 400,237 400,420 0,490" fill="url(#orangeBand)"/>
    </svg>

    <svg class="rollup__photo" viewBox="0 0 400 940" role="img"
         aria-label="Photo: smiling delivery man in red cap and polo holding a blue crate of fresh vegetables and milk, in front of a Sardinian marina with yachts and hills">
      <defs>
        <linearGradient id="photoTones" x1="0" y1="0" x2="0" y2="1">
          <stop offset="0" stop-color="#8fc6e6"/>
          <stop offset="0.3" stop-color="#4d6f8c"/>
          <stop offset="0.55" stop-color="#b03a30"/>
          <stop offset="0.75" stop-color="#2c55c8"/>
          <stop offset="1" stop-color="#8f8a62"/>
        </linearGradient>
      </defs>
      <polygon points="0,495 400,473 400,820 0,892" fill="url(#photoTones)"/>
    </svg>

    <header class="brand">
      <div class="brand__main">
        <span class="brand__dot"></span>
        <span class="brand__name">The Velarno</span>
      </div>
      <span class="brand__partner">Calvesinoshop</span>
    </header>

    <h1 class="headline">
      <span class="headline__line">CONSEGNA</span>
      <span class="headline__line">STESSO</span>
      <span class="headline__line">GIORNO</span>
    </h1>

    <div class="phone">
      <span class="phone__icon">
        <svg width="20" height="20" viewBox="0 0 24 24" aria-hidden="true">
          <path d="M6.6 10.8a15.1 15.1 0 0 0 6.6 6.6l2.2-2.2a1 1 0 0 1 1-.25 11.4 11.4 0 0 0 3.6.57 1 1 0 0 1 1 1V20a1 1 0 0 1-1 1A17 17 0 0 1 3 4a1 1 0 0 1 1-1h3.5a1 1 0 0 1 1 1 11.4 11.4 0 0 0 .57 3.6 1 1 0 0 1-.25 1z" fill="var(--ink)"/>
        </svg>
      </span>
      <span class="phone__number">0321 654 987</span>
    </div>
  </main>
</body>
</html>
```